Brent Oakes Director / Photographer Branding

I need note pads, envelops, business cards and letter head for my company. I'm a fashion and advertising director / photographer. I'm having trouble deciding how to include both Director & Photographer in my title or if it is even necessary. Maybe just my name is enough. I'm open for even using my initials if it works with the design and overall pieces. Please view my website to see what I have at this moment and what work I do. www.brentoakesstudio-mail.net
Updates

Project Deadline Extended
Reason: Hello Everyone! I'm extending the deadline since I have been traveling on a job out of country and I wanted to have more time to look through all the designs and give enough time for everyone to provide changes with designs and updates. I will be more available to communicate online now that I'm back in the office! Thank you! Brent Oakes

Target Market(s)

Fashion magazines, clothing lines and beauty cosmetic brands.

Industry/Entity Type

Fashion Photography

Font styles to use
Sans Serif

Colors
acd036
acd35d
cbcbcb
f5f5f5

Requirements
Must have
• My name.. Brent Oakes, my website: brentoakesstudio-mail.net my phone number, 555-284-6103
• I don't need my address on these. I also live by the philosophy that less is more and keeping things simple ads strength to a design. I also don't want to stop people from taking chances and experimenting with an idea that might take me down different road with my branding.
Nice to have
• Bold designs and clean lines. I'm open to ideas that I could adopt but I lean towards a more minimalistic look in general.
Should not have
• Not have cheesy graphics or pictures. No images of cameras, film or anything that looks like it is a camera or aperture, lens etc... ;)

```html
<!DOCTYPE html>
<html lang="en">
<head>
<meta charset="utf-8">
<title>Brent Oakes — Stationery</title>
<link href="https://fonts.googleapis.com/css2?family=Advent+Pro:wght@200;300&family=Michroma&family=Open+Sans:wght@400;600&display=swap" rel="stylesheet">
<style>
  :root {
    --lime: #acd036;
    --lime-soft: #acd35d;
    --grey: #cbcbcb;
    --grey-dark: #8a8d90;
    --paper: #ffffff;
    --off-white: #f5f5f5;
    --backdrop: #e3f78f;
    --flap: #3b4043;
    --ink: #6f7478;
  }
  * { box-sizing: border-box; margin: 0; padding: 0; }
  html, body { width: 1200px; height: 900px; overflow: hidden; }
  body {
    background: radial-gradient(circle at 50% 45%, #e8f9a4 0%, var(--backdrop) 70%);
    font-family: "Open Sans", sans-serif;
    position: relative;
  }
  .piece { position: absolute; box-shadow: 0 6px 18px rgba(80, 110, 0, 0.18); }

  /* Note sheet */
  .note-sheet { left: 60px; top: 50px; width: 460px; height: 280px; background: var(--paper); }
  .note-sheet .corner-bar { position: absolute; left: 0; top: 0; width: 6px; height: 70px; background: var(--grey-dark); }
  .note-sheet .name { position: absolute; left: 30px; top: 30px; font-family: "Michroma", sans-serif; font-size: 24px; color: var(--lime); letter-spacing: 2px; }
  .note-sheet .title { position: absolute; left: 30px; top: 66px; font-family: "Advent Pro", sans-serif; font-weight: 300; font-size: 17px; color: var(--grey); }
  .note-sheet .contacts { position: absolute; left: 24px; right: 24px; bottom: 22px; display: flex; justify-content: space-between; }
  .note-sheet .footer-strip { position: absolute; left: 0; right: 0; bottom: 0; height: 5px; background: var(--lime); }
  .note-sheet .footer-grey { position: absolute; left: 0; bottom: 0; width: 60px; height: 5px; background: var(--grey-dark); }

  .contact { display: flex; flex-direction: column; align-items: center; gap: 3px; font-size: 8px; color: var(--ink); }
  .contact svg { width: 10px; height: 10px; fill: var(--lime); }

  /* Envelope */
  .envelope { left: 60px; top: 370px; width: 460px; height: 250px; background: var(--lime); }
  .envelope svg { position: absolute; inset: 0; }

  /* Pencil-free, letterhead */
  .letterhead { left: 620px; top: 40px; width: 400px; height: 520px; background: var(--paper); }
  .letterhead .corner-top { position: absolute; left: 0; top: 0; width: 60px; height: 5px; background: var(--grey-dark); }
  .letterhead .corner-right { position: absolute; right: 0; top: 110px; width: 5px; height: 40px; background: var(--grey-dark); }
  .letterhead .corner-bottom { position: absolute; left: 0; bottom: 0; width: 5px; height: 60px; background: var(--grey-dark); }
  .letterhead .spine { position: absolute; left: 14px; top: 20px; bottom: 20px; display: flex; flex-direction: column; justify-content: space-between; font-family: "Michroma", sans-serif; font-size: 22px; color: var(--grey-dark); }
  .letterhead .head-name { position: absolute; left: 70px; top: 26px; font-family: "Michroma", sans-serif; font-size: 11px; color: var(--lime); letter-spacing: 1px; }
  .letterhead .head-title { position: absolute; left: 70px; top: 42px; font-family: "Advent Pro", sans-serif; font-size: 10px; color: var(--grey); }
  .letterhead .rule { position: absolute; left: 70px; right: 30px; top: 62px; height: 3px; background: var(--lime); }
  .letterhead .head-contacts { position: absolute; right: 30px; top: 72px; text-align: right; font-size: 7px; color: var(--ink); line-height: 1.6; }
  .dot { display: inline-block; width: 5px; height: 5px; background: var(--lime); margin-right: 3px; vertical-align: middle; }
  .letterhead .base { position: absolute; left: 0; right: 0; bottom: -14px; height: 14px; background: var(--lime); }

  /* Business cards */
  .card { width: 300px; height: 170px; }
  .card-front { left: 580px; top: 630px; background: var(--lime); }
  .card-front .band { position: absolute; left: 0; right: 0; top: 30px; height: 70px; background: var(--paper); display: flex; align-items: center; justify-content: center; }
  .card-front .band span { font-family: "Advent Pro", sans-serif; font-weight: 200; font-size: 34px; color: var(--lime); letter-spacing: 1px; }
  .card-front .web { position: absolute; left: 0; right: 0; top: 116px; text-align: center; font-size: 8px; color: var(--paper); }
  .card-front .web svg { width: 9px; height: 9px; fill: var(--paper); display: block; margin: 0 auto 3px; }

  .card-back { left: 900px; top: 630px; background: var(--paper); overflow: hidden; }
  .card-back .lower { position: absolute; left: 0; right: 0; bottom: 0; height: 90px; background: var(--lime); }
  .card-back .notch { position: absolute; left: 70px; width: 14px; height: 8px; background: var(--lime); clip-path: polygon(0 0, 100% 0, 50% 100%); }
  .card-back .notch.top { top: 0; }
  .card-back .notch.mid { top: 80px; background: var(--paper); }
  .card-back .name { position: absolute; left: 22px; top: 34px; font-family: "Advent Pro", sans-serif; font-weight: 200; font-size: 30px; color: var(--lime); }
  .card-back .title { position: absolute; left: 24px; top: 90px; font-family: "Advent Pro", sans-serif; font-size: 11px; color: var(--paper); }
  .card-back .details { position: absolute; right: 16px; bottom: 12px; font-size: 7.5px; color: var(--paper); line-height: 1.7; text-align: left; }
  .card-back .details .dot { background: var(--paper); }
</style>
</head>
<body>

  <section class="piece note-sheet">
    <div class="corner-bar"></div>
    <div class="name">BRENT OAKES</div>
    <div class="title">Director / Photographer</div>
    <div class="contacts">
      <div class="contact"><svg viewBox="0 0 10 10"><path d="M0 2h10v6H0z M0 2l5 3.5L10 2" /></svg>hello@brentoakesstudio-mail.net</div>
      <div class="contact"><svg viewBox="0 0 10 10"><path d="M2 0h2l1 3-1.5 1a6 6 0 0 0 2.5 2.5L7 5l3 1v2c0 1-1 2-2 2C3.5 10 0 6.5 0 2c0-1 1-2 2-2z"/></svg>555-284-6103</div>
      <div class="contact"><svg viewBox="0 0 10 10"><circle cx="5" cy="5" r="5"/></svg>www.brentoakesstudio-mail.net</div>
      <div class="contact"><svg viewBox="0 0 10 10"><rect width="10" height="10"/></svg>@brentoakesstudio</div>
    </div>
    <div class="footer-strip"></div>
    <div class="footer-grey"></div>
  </section>

  <section class="piece envelope">
    <svg viewBox="0 0 460 250" width="460" height="250">
      <polygon points="30,20 430,20 400,70 60,70" fill="var(--flap)"/>
    </svg>
  </section>

  <section class="piece letterhead">
    <div class="corner-top"></div>
    <div class="corner-right"></div>
    <div class="corner-bottom"></div>
    <div class="spine"><span>B</span><span>R</span><span>E</span><span>N</span><span>T</span><span>O</span><span>A</span><span>K</span><span>E</span><span>S</span></div>
    <div class="head-name">BRENT OAKES</div>
    <div class="head-title">Director / Photographer</div>
    <div class="rule"></div>
    <div class="head-contacts">
      <span class="dot"></span>hello@brentoakesstudio-mail.net &nbsp; <span class="dot"></span>555-284-6103<br>
      <span class="dot"></span>www.brentoakesstudio-mail.net &nbsp; <span class="dot"></span>@brentoakesstudio
    </div>
  </section>

  <section class="piece card card-front">
    <div class="band"><span>BRENT OAKES</span></div>
    <div class="web"><svg viewBox="0 0 10 10"><circle cx="5" cy="5" r="5"/></svg>www.brentoakesstudio-mail.net</div>
  </section>

  <section class="piece card card-back">
    <div class="lower"></div>
    <div class="notch top"></div>
    <div class="notch mid"></div>
    <div class="name">BRENT OAKES</div>
    <div class="title">Director / Photographer</div>
    <div class="details">
      <span class="dot"></span>hello@brentoakesstudio-mail.net<br>
      <span class="dot"></span>555-284-6103<br>
      <span class="dot"></span>www.brentoakesstudio-mail.net<br>
      <span class="dot"></span>@brentoakesstudio
    </div>
  </section>

</body>
</html>
```